Supplement business needs a label design

We need a label design for our company VANTRELO LLC in The Woodlands, Texas,
This label is for a Fish Oil supplement.
Here is the task:
1. The text needs to be bold and readable on smartphone ads
2. The background is in a basic standard color like blue, silver, black, brown, etc
3. A watermark is on the background-color (waves, leaves, etc.).
4. The Brand will be "V A N T R E L O" with the attached logo design and "CU T T I N G E D G E F O R MU L A SU P P L E M E N T " :
5. Further details have to be on the label like on the attached Fish oil sample: "450 E P A / 300 D H A 1 , 2 5 0 M G DIETARY SUPPLEMENT GLUTENFREE with the icon and heart icon.
6. Please see attached samples:

```html
<!DOCTYPE html>
<html lang="en">
<head>
<meta charset="utf-8">
<title>VANTRELO Lifestyle Omega 3 Label</title>
<link rel="stylesheet" href="https://fonts.googleapis.com/css2?family=Montserrat:wght@500;600;700&family=Pinyon+Script&display=swap">
<style>
  :root {
    --page: #ffffff;
    --label-white: #f7f8f9;
    --blue: #2a78c0;
    --blue-deep: #0f4f8c;
    --blue-light: #5aa6db;
    --silver: #c7ccd2;
    --silver-dark: #8e969f;
    --orange: #e8883a;
    --orange-deep: #c95a14;
    --ink: #2b2b2b;
    --fish-light: #e6eaec;
    --fish-mid: #bfc7cb;
  }
  html, body {
    margin: 0;
    padding: 0;
    width: 1200px;
    height: 1200px;
    overflow: hidden;
    background: var(--page);
  }
  .canvas {
    position: relative;
    width: 1200px;
    height: 1200px;
  }
  .label {
    position: absolute;
    left: 156px;
    top: 40px;
    width: 888px;
    height: 1120px;
    box-shadow: 0 4px 18px rgba(0,0,0,0.12);
  }
  .label svg { display: block; width: 100%; height: 100%; }
  .brand-name {
    font-family: "Montserrat", sans-serif;
    font-weight: 700;
    font-size: 42px;
    fill: #ffffff;
  }
  .product-script {
    font-family: "Pinyon Script", cursive;
    font-size: 50px;
    fill: var(--ink);
  }
  .product-name {
    font-family: "Montserrat", sans-serif;
    font-weight: 600;
    font-size: 80px;
    fill: var(--orange);
    letter-spacing: -2px;
  }
  .product-number {
    font-family: "Montserrat", sans-serif;
    font-weight: 600;
    font-size: 240px;
    fill: var(--orange-deep);
  }
  .product-sub {
    font-family: "Montserrat", sans-serif;
    font-weight: 600;
    font-size: 23px;
    letter-spacing: 4px;
    fill: var(--ink);
  }
  .footer-text {
    font-family: "Montserrat", sans-serif;
    font-weight: 600;
    font-size: 17px;
    fill: #ffffff;
  }
  .badge-text {
    font-family: "Montserrat", sans-serif;
    font-weight: 500;
    font-size: 10px;
    fill: #ffffff;
  }
</style>
</head>
<body>
<div class="canvas">
  <div class="label">
    <svg viewBox="0 0 606 765" xmlns="http://www.w3.org/2000/svg">
      <defs>
        <linearGradient id="topBand" x1="0" y1="0" x2="1" y2="0">
          <stop offset="0" stop-color="var(--blue-light)"/>
          <stop offset="0.5" stop-color="var(--blue-deep)"/>
          <stop offset="1" stop-color="var(--blue-light)"/>
        </linearGradient>
        <linearGradient id="bottomBand" x1="0" y1="0" x2="1" y2="0">
          <stop offset="0" stop-color="var(--blue-light)"/>
          <stop offset="0.5" stop-color="var(--blue)"/>
          <stop offset="1" stop-color="var(--blue-deep)"/>
        </linearGradient>
        <linearGradient id="fishTone" x1="0" y1="0" x2="1" y2="1">
          <stop offset="0" stop-color="var(--fish-light)"/>
          <stop offset="1" stop-color="var(--fish-mid)"/>
        </linearGradient>
      </defs>

      <rect class="label-base" width="606" height="765" fill="var(--label-white)"/>

      <!-- header chevron -->
      <polygon points="0,0 606,0 606,70 304,280 0,70" fill="var(--silver)"/>
      <polygon points="0,0 606,0 606,55 304,248 0,55" fill="url(#topBand)"/>
      <polygon points="70,0 536,0 304,60" fill="var(--silver)" opacity="0.6"/>

      <!-- brand -->
      <circle cx="172" cy="113" r="20" fill="none" stroke="#ffffff" stroke-width="3"/>
      <text class="brand-name" x="206" y="128">VANTRELO</text>

      <!-- product visual area -->
      <path role="img" aria-label="Photograph of a leaping salmon" d="M40,405 C90,330 220,300 330,305 C420,308 470,340 500,400 C530,460 560,520 558,600 C520,560 490,520 460,505 C360,470 150,450 40,405 Z" fill="url(#fishTone)" opacity="0.85"/>

      <!-- product title -->
      <text class="product-script" x="96" y="352">Lifestyle</text>
      <text class="product-name" x="86" y="452">OMEGA</text>
      <text class="product-number" x="366" y="512">3</text>
      <text class="product-sub" x="88" y="494">WITH EPA &amp; DHA</text>

      <!-- footer band -->
      <path d="M0,540 C150,620 380,650 606,660 L606,765 L0,765 Z" fill="var(--silver)"/>
      <path d="M0,550 C150,630 380,662 606,670 L606,740 L0,740 Z" fill="url(#bottomBand)"/>
      <rect y="740" width="606" height="25" fill="var(--silver-dark)" opacity="0.7"/>

      <!-- heart icon -->
      <g class="heart-icon" fill="none" stroke="var(--orange)" stroke-width="3" stroke-linejoin="round" stroke-linecap="round">
        <path d="M110,700 L76,664 C60,646 66,616 90,614 C100,613 107,620 110,628 C113,620 120,613 130,614 C154,616 160,646 144,664"/>
        <polyline points="70,648 88,648 96,630 106,668 114,644 134,644"/>
        <circle cx="132" cy="690" r="17"/>
        <line x1="132" y1="680" x2="132" y2="700"/>
        <line x1="122" y1="690" x2="142" y2="690"/>
      </g>

      <text class="footer-text" x="201" y="708">DIETARY SUPPLEMENT</text>

      <!-- gluten free badge -->
      <circle cx="498" cy="650" r="40" fill="var(--orange)"/>
      <line x1="470" y1="690" x2="528" y2="610" stroke="var(--silver)" stroke-width="2"/>
      <text class="badge-text" x="463" y="715">GULTEN FREE</text>
    </svg>
  </div>
</div>
</body>
</html>
```